Graphics for Vorlani telehealth weight loss plans

Vorlani focuses on delivering medical weight-loss using prescription medicine and telehealth consults. Vorlani needs graphics for its ecommerce site for three weight loss plans. The plans are posted here with current graphics and descriptions of what is included with each plan. Please do not feel constrained by current graphics or styling.

- https://shop.vorlanicare.com/products/steady-horizon-plan
- https://shop.vorlanicare.com/products/amber-ridge-plan
- https://shop.vorlanicare.com/products/calm-harbor-plan

The graphics need to look good on mobile and desktop browsers.

```html
<!DOCTYPE html>
<html lang="en">
<head>
<meta charset="utf-8">
<title>Amber Ridge Plan – Vorlani</title>
<link href="https://fonts.googleapis.com/css2?family=Oswald:wght@400;500;600;700&family=Source+Sans+3:wght@400;600;700&display=swap" rel="stylesheet">
<style>
  :root{
    --ink:#121212;
    --muted:#4a4a4a;
    --navy:#252361;
    --sky:#29cbfc;
    --photo-dark:#6f6f6f;
    --photo-light:#c9c9c9;
    --white:#ffffff;
  }
  *{box-sizing:border-box;margin:0;padding:0}
  html,body{width:1200px;height:801px;overflow:hidden;background:var(--white)}
  body{position:relative;font-family:"Source Sans 3",sans-serif;color:var(--ink)}

  .site-header{position:absolute;left:0;top:0;width:1200px;height:140px}
  .brand{position:absolute;left:89px;top:58px;display:flex;align-items:center;gap:6px;font-size:19px;font-weight:600;color:var(--ink);letter-spacing:.3px}
  .brand-mark{width:12px;height:12px;background:var(--ink)}
  .main-nav{position:absolute;left:177px;top:58px;display:flex;gap:26px;font-size:15px;letter-spacing:.5px;color:#333}
  .main-nav span{display:flex;align-items:center;gap:6px}
  .header-icons{position:absolute;left:1030px;top:58px;display:flex;gap:24px}
  .header-icons svg{width:22px;height:22px;stroke:var(--ink);fill:none;stroke-width:1.6}

  .plan-graphic{position:absolute;left:79px;top:138px;width:482px;height:623px;background:var(--sky)}
  .plan-photo{position:absolute;left:0;top:0;width:482px;height:199px;background:linear-gradient(100deg,var(--photo-dark) 0%,var(--photo-light) 45%,#9a9a9a 100%)}
  .plan-card{position:absolute;left:0;top:137px;width:370px;height:62px;background:var(--sky)}
  .plan-title{position:absolute;left:33px;top:142px;font-family:"Oswald",sans-serif;font-weight:700;font-size:58px;line-height:54px;color:var(--navy);letter-spacing:-.5px}
  .plan-sub{position:absolute;left:33px;top:257px;font-family:"Oswald",sans-serif;font-weight:500;font-size:27px;line-height:31px;color:var(--navy);letter-spacing:-.3px}
  .includes-tag{position:absolute;left:33px;top:332px;padding:1px 9px;background:var(--navy);color:var(--white);font-family:"Oswald",sans-serif;font-weight:500;font-size:19px;line-height:25px}
  .feature{position:absolute;font-family:"Oswald",sans-serif;color:var(--navy);font-weight:500;font-size:20px;line-height:23px}
  .feature::before{content:"";position:absolute;left:-11px;top:10px;width:5px;height:5px;border-radius:50%;background:var(--navy)}
  .feature small{font-size:15px;font-weight:400}
  .feature .note{display:block;font-size:15px;font-weight:400;line-height:17px}
  .pay-badge{position:absolute;left:31px;top:531px;height:55px;display:flex;align-items:center}
  .pay-icon{width:55px;height:55px;border-radius:50%;background:var(--navy);display:flex;align-items:center;justify-content:center;position:relative;z-index:1}
  .pay-icon svg{width:32px;height:32px;stroke:var(--white);fill:none;stroke-width:2}
  .pay-label{margin-left:-6px;padding:2px 14px 2px 19px;background:var(--navy);color:var(--white);font-family:"Oswald",sans-serif;font-size:18px;line-height:23px}

  .product-info{position:absolute;left:614px;top:140px;width:540px}
  .product-title{font-size:44px;font-weight:400;line-height:52px;letter-spacing:.4px}
  .price{margin-top:22px;font-size:18px;letter-spacing:.8px}
  .billing{margin-top:25px;font-size:18.5px;color:var(--muted);letter-spacing:.4px}
  .reorder{margin-top:22px;font-size:16px;color:var(--muted);letter-spacing:.4px}
  .buy-button{display:block;margin-top:26px;width:468px;height:51px;background:var(--ink);color:var(--white);border:none;font-family:inherit;font-size:15.5px;letter-spacing:1px}
  .description{margin-top:24px;font-size:16.5px;line-height:30.5px;color:var(--muted);letter-spacing:.3px}
  .description p{margin-bottom:17px}
  .description strong{color:#333;font-weight:700}
  .description ul{margin-left:20px}
</style>
</head>
<body>
  <header class="site-header">
    <div class="brand"><span class="brand-mark"></span>Vorlani</div>
    <nav class="main-nav">
      <span>Testimonials</span>
      <span>Help <svg width="10" height="6" viewBox="0 0 10 6"><path d="M1 1l4 4 4-4" stroke="#333" fill="none" stroke-width="1.3"/></svg></span>
      <span>About</span>
      <span>Contact</span>
    </nav>
    <div class="header-icons">
      <svg viewBox="0 0 24 24"><circle cx="10" cy="10" r="7"/><path d="M15 15l7 7"/></svg>
      <svg viewBox="0 0 24 24"><circle cx="12" cy="7" r="4.5"/><path d="M3 22v-3c0-3 3-5 9-5s9 2 9 5v3z"/></svg>
      <svg viewBox="0 0 24 24"><path d="M3 7h18v15H3z"/><path d="M8 10V5a4 4 0 0 1 8 0v5"/></svg>
    </div>
  </header>

  <section class="plan-graphic">
    <div class="plan-photo" role="img" aria-label="Black and white photo of a measuring tape around a waist with capsules scattered beside it"></div>
    <div class="plan-card"></div>
    <h2 class="plan-title">AMBER RIDGE<br>PLAN</h2>
    <p class="plan-sub">PHYSICIAN CONSULTATION<br>PHENTERMINE PROGRAM</p>
    <span class="includes-tag">Includes</span>
    <p class="feature" style="left:40px;top:372px">100% online.<span class="note">No need to visit the office.</span></p>
    <p class="feature" style="left:40px;top:419px">Phentermine<br>prescription.</p>
    <p class="feature" style="left:40px;top:471px">Medical<br>consultation.</p>
    <p class="feature" style="left:231px;top:367px">Real Phentermine <small>(37.5mg/Pill)</small><br>delivered to your door.</p>
    <p class="feature" style="left:231px;top:429px">1 month supply. <small>(30 pills)</small></p>
    <p class="feature" style="left:231px;top:468px">FREE Introductory Nutritionist<br>consult on your first month.</p>
    <div class="pay-badge">
      <span class="pay-icon"><svg viewBox="0 0 32 32"><ellipse cx="16" cy="12" rx="10" ry="6"/><path d="M6 12v5c0 3 4 6 10 6"/><path d="M20 26l4-3-4-3"/></svg></span>
      <span class="pay-label">Month-to-month pay as you go.</span>
    </div>
  </section>

  <section class="product-info">
    <h1 class="product-title">Amber Ridge Plan</h1>
    <p class="price">$119.00</p>
    <p class="billing">No recurring billing</p>
    <p class="reorder">You're always in control of when you reorder.</p>
    <button class="buy-button">Buy it now</button>
    <div class="description">
      <p>The <strong>Amber Ridge Plan</strong> includes <strong>real Phentermine (37.5mg / pill)</strong>. You get a 1 month supply (30 pills, 1 pill per day).</p>
      <p>This program is designed for people who need some help with caloric restriction, but otherwise believe that they know how to approach their diet. Even if you have tried dieting in the past, and feel self assured that you don't need additional help, you may still benefit from a professional consultation, so we have included a free introductory Nutritionist consult.</p>
      <p><strong>Plan includes:</strong></p>
      <ul><li><strong>100% online</strong>. No need to visit the office.</li></ul>
    </div>
  </section>
</body>
</html>
```